Business Card Design Project

Business card incoporating newly designed logo. The business cards will be magnets and I would like the same design as previously provided (Blue colour swatch with logo up the top) Please note that the logo incorporates a website so it needs to be legible.
The blue colours in teh swatch ideally will be in the same range as the blue of the logo.
The copy should all be in the same colour ie. black if in the white lines or white if in the swatch itself
Updates

Hi All

Some of the designs are very close to what I am after.  I have added logo and updated brief to assist with design.  This project is not refundable so I will be selecting a design.

Hi All

We are looking for a business card as per the brief (colour swatch style) as mentioned it is also a magnet so it needs to be created to the specs supplied.  Being a magnet there is also no requirment for reverse design.

Cheers
Marcy

Industry/Entity Type

Business

Requirements
Must have
• Blue colour swatch design. (see attached current example)
KW Coatings logo (colour) up the top
I require 1 design but 2 versions (with two peoples names and mobile numbers)

The magnets will be printed by PrintHollow.com.au And you can find the full specs online http://www.printhollow.com.au/custom-magnets.aspx

```html
<!DOCTYPE html>
<html lang="en">
<head>
<meta charset="utf-8">
<title>House Painting – Business Card</title>
<link rel="stylesheet" href="https://fonts.googleapis.com/css2?family=Arimo:wght@400;700&display=swap">
<style>
  :root {
    --page-bg: #e9e6e2;
    --brand-blue: #2a1872;
    --swatch-text: #dcdcde;
    --panel-light: #f4f4f4;
    --panel-mid: #e6e6e6;
    --ink: #444444;
    --icon-bg: #4a4a4a;
    --pointer: #a9a9a9;
  }
  * { margin: 0; padding: 0; box-sizing: border-box; }
  html, body {
    width: 1200px;
    height: 970px;
    overflow: hidden;
    background: var(--page-bg);
    font-family: "Arimo", Arial, sans-serif;
  }
  .business-card {
    position: absolute;
    left: 168px;
    top: 268px;
    width: 863px;
    height: 482px;
    border-radius: 24px;
    overflow: hidden;
    background: linear-gradient(90deg, var(--panel-mid) 0%, var(--panel-light) 45%, var(--panel-mid) 100%);
    box-shadow: 0 6px 18px rgba(0,0,0,0.12);
  }
  .brand-swatch {
    position: absolute;
    left: 0; top: 0;
    width: 100%;
    height: 216px;
    background: var(--brand-blue);
    text-align: center;
    color: var(--swatch-text);
  }
  .brand-name {
    position: absolute;
    left: 0; right: 0;
    top: 50px;
    font-size: 79px;
    font-weight: 400;
    line-height: 1;
    letter-spacing: -0.5px;
    padding-left: 8px;
  }
  .brand-tagline {
    position: absolute;
    left: 0; right: 0;
    top: 146px;
    font-size: 21px;
    font-weight: 700;
    letter-spacing: 4.6px;
    padding-left: 10px;
  }
  .bottom-band {
    position: absolute;
    left: 0; bottom: 0;
    width: 100%;
    height: 28px;
    background: var(--brand-blue);
  }
  .pointer {
    position: absolute;
    left: 0;
    top: 244px;
    width: 20px;
    height: 34px;
  }
  .contact-block {
    position: absolute;
    left: 78px;
    top: 234px;
    color: var(--ink);
  }
  .person-name {
    font-size: 46px;
    font-weight: 700;
    line-height: 1;
  }
  .person-role {
    margin-top: 8px;
    font-size: 30px;
    line-height: 1;
  }
  .contact-list {
    list-style: none;
    margin-top: 35px;
  }
  .contact-item {
    display: flex;
    align-items: center;
    font-size: 29px;
    line-height: 36px;
  }
  .contact-icon {
    width: 24px;
    height: 24px;
    margin-right: 20px;
    flex: none;
  }
</style>
</head>
<body>
  <main class="business-card">
    <header class="brand-swatch">
      <h1 class="brand-name">House Painting</h1>
      <p class="brand-tagline">Commercial &amp; Domestic Painting</p>
    </header>

    <svg class="pointer" viewBox="0 0 20 34" aria-hidden="true">
      <polygon points="0,0 20,17 0,34" fill="var(--pointer)"/>
    </svg>

    <section class="contact-block">
      <h2 class="person-name">Owen Hartley</h2>
      <p class="person-role">Interiors &amp; Exteriors</p>
      <ul class="contact-list">
        <li class="contact-item">
          <svg class="contact-icon" viewBox="0 0 24 24" aria-hidden="true">
            <rect width="24" height="24" rx="3" fill="var(--icon-bg)"/>
            <path d="M7.5 5.5c.6-.4 1.3-.3 1.7.3l1.3 2c.3.5.2 1.2-.3 1.6l-.9.7c.7 1.6 1.9 2.9 3.5 3.7l.8-.9c.4-.5 1.1-.6 1.6-.2l2 1.3c.6.4.7 1.1.3 1.7l-.8 1.1c-.6.8-1.6 1.1-2.6.8-4-1.3-7-4.4-8.2-8.4-.3-1 .1-2 .8-2.6z" fill="#fff"/>
          </svg>
          <span>0412 555 208</span>
        </li>
        <li class="contact-item">
          <svg class="contact-icon" viewBox="0 0 24 24" aria-hidden="true">
            <rect width="24" height="24" rx="3" fill="var(--icon-bg)"/>
            <text x="12" y="17" text-anchor="middle" font-family="Arimo, Arial, sans-serif" font-size="15" font-weight="700" fill="#fff">@</text>
          </svg>
          <span>owenhartleypainting@mailpost.com</span>
        </li>
      </ul>
    </section>

    <div class="bottom-band"></div>
  </main>
</body>
</html>
```